need web page design for TarnwickHub.com

This site sells information products for international corporate users. It is selling Silent Rivers and Quiet Orchard Lanes, a product on international business tax, and other books. See sample. I will also upload a possible logo. Upload 2 The tag line is Predicting and Solving Business and Law Issues for the Multinational Upload 3 is a sample theme from Shopify, the site I will use. The sample is for ideas only. I am not wedded to it. Upload 4 is Copperfield Monthly Digest Pge

2 page

```html
<!DOCTYPE html>
<html lang="en">
<head>
<meta charset="utf-8">
<title>TarnwickHub.com</title>
<link rel="stylesheet" href="https://fonts.googleapis.com/css2?family=Open+Sans:wght@400;600;700&display=swap">
<style>
:root{
  --navy:#0a2473;
  --grey:#7a7a7a;
  --grey-mid:#8c8c8c;
  --grey-light:#f3f3f3;
  --line:#d5d5d5;
  --text:#333;
  --white:#fff;
}
*{box-sizing:border-box;margin:0;padding:0}
html,body{width:767px;height:1200px;overflow:hidden;background:var(--white)}
body{font-family:"Open Sans",Arial,sans-serif;color:var(--text)}
.page{position:relative;width:767px;height:1200px;overflow:hidden}
.abs{position:absolute}

.top-strip{left:0;top:0;width:767px;height:17px;background:var(--navy)}
.social{right:64px;top:4px;display:flex;gap:4px}
.social span{width:10px;height:10px;background:var(--white);border-radius:1px}

.brand{display:flex;align-items:center;gap:6px;font-weight:700;color:var(--navy);white-space:nowrap}
.brand .dot{border-radius:50%;background:var(--navy)}
.header-brand{left:66px;top:40px;font-size:15px}
.header-brand .dot{width:26px;height:26px}

.nav{left:246px;top:62px;width:460px;height:26px;background:#4a4a4a;display:flex;align-items:center;font-size:8px;color:#ddd;border-radius:2px 2px 0 0}
.nav a{color:#ddd;text-decoration:none;padding:0 14px;height:26px;line-height:26px}
.nav a.active{background:var(--navy);color:var(--white);padding:0 19px;margin-left:2px}
.search{position:absolute;right:22px;top:6px;width:106px;height:15px;background:var(--white);font-size:7px;color:#aaa;padding-left:5px;line-height:15px}
.search-btn{position:absolute;right:4px;top:5px;width:18px;height:17px;background:var(--navy)}

.hero-band{left:0;top:88px;width:767px;height:278px;background:var(--navy)}
.hero-title{left:0;top:100px;width:767px;text-align:center;color:var(--white);font-size:23px;font-weight:600;font-variant:small-caps;letter-spacing:.5px}
.slide{left:62px;top:138px;width:644px;height:287px;border:1px solid #aaa;background:linear-gradient(100deg,#ffffff 0%,#f4f1ec 45%,#e9d2ad 70%,#d8b58e 100%)}
.arrow{top:251px;width:51px;height:39px;display:flex;align-items:center;justify-content:center}
.arrow.prev{left:55px;background:#8a8a8a}
.arrow.next{left:662px;background:#1f4fc4}
.dots{left:652px;top:402px;display:flex;gap:2px}
.dots span{width:12px;height:12px;border-radius:50%;background:var(--white)}
.dots span.on{background:var(--navy)}

.services-tab{left:319px;top:445px;width:126px;height:30px;background:var(--navy);border:1px solid #4c63a8;color:var(--white);display:flex;align-items:center;justify-content:space-between;padding:0 8px;font-weight:700;font-size:15px;font-variant:small-caps}

.service{top:494px;width:160px;text-align:center}
.service .icon{width:82px;height:82px;margin:0 auto;border-radius:50%;border:2px solid var(--grey-mid);display:flex;align-items:center;justify-content:center}
.service.active .icon{border-color:var(--navy)}
.service h3{margin-top:21px;font-size:10px;font-weight:700;color:#666}
.service.active h3{color:var(--navy)}
.service p{margin-top:9px;height:30px;font-size:7.5px;line-height:10px;color:#888;padding:0 30px}
.service.active p{color:var(--navy)}
.btn{display:inline-block;color:var(--white);font-size:7.5px;text-align:center;background:var(--grey)}
.service .btn{margin-top:16px;width:78px;height:28px;line-height:28px}
.service.active .btn,.btn.navy{background:var(--navy)}

.pager{left:216px;top:718px;width:344px;display:flex;align-items:center;gap:30px;font-size:13px;color:#555}
.pager i{flex:1;height:2px;background:var(--grey-mid)}
.pager b{color:var(--navy)}

.divider{left:0;top:752px;width:767px;height:1px;background:var(--line)}

.welcome{left:64px;top:766px;width:290px}
.welcome h2{font-size:24px;font-weight:700;color:var(--navy)}
.welcome h4{margin-top:6px;font-size:14.5px;font-weight:400;color:var(--navy);line-height:18px}
.welcome p{margin-top:8px;width:280px;font-size:7.5px;line-height:10.5px;color:#444}
.welcome .btn{margin-top:18px;width:77px;height:27px;line-height:27px}
.office{left:388px;top:761px;width:320px;height:183px;border:1px solid #bbb;background:linear-gradient(110deg,#dfe4ea 0%,#c4ccd5 35%,#eadccd 65%,#f1e6da 100%)}

.newsletter{left:0;top:954px;width:767px;height:52px;background:linear-gradient(#9a9a9a,#6e6e6e)}
.newsletter h3{position:absolute;left:97px;top:13px;color:var(--white);font-size:21px;font-weight:400}
.field{height:27px;background:var(--white);font-size:9px;font-weight:600;color:#999;padding-left:9px;line-height:27px}
.nl-name{left:226px;top:968px;width:171px}
.nl-mail{left:404px;top:968px;width:172px}
.subscribe{left:588px;top:968px;width:76px;height:27px;line-height:27px;background:var(--navy);color:var(--white);font-size:9.5px;font-weight:700;text-align:center}

.footer{left:0;top:1006px;width:767px;height:182px;background:var(--grey-light)}
.footer-brand{left:62px;top:1046px;font-size:11px}
.footer-brand .dot{width:18px;height:18px}
.footer-about{left:63px;top:1099px;width:200px;font-size:6.5px;line-height:8px;color:#777}
.col-title{font-size:10px;font-weight:600;color:#666;white-space:nowrap}
.quick{left:319px;top:1028px;width:68px}
.quick ul{list-style:none;margin-top:8px}
.quick li{font-size:7.5px;color:#777;height:16.5px;line-height:14px;border-bottom:1px solid var(--line)}
.twitter{left:505px;top:1028px}
.tw-field{width:144px;height:19px;background:#bdbdbd;font-size:7px;color:#666;padding-left:6px;line-height:19px;margin-top:11px}
.twitter .col-title+.tw-field{margin-top:8px}
.contact{left:507px;top:1127px;display:flex;gap:8px;align-items:center}
.contact p{font-size:7.5px;line-height:17px;color:#777}
.bottom-strip{left:0;top:1188px;width:767px;height:12px;background:var(--navy)}
</style>
</head>
<body>
<div class="page">
  <div class="abs top-strip"></div>
  <div class="abs social"><span></span><span></span><span></span><span></span><span></span></div>

  <div class="abs brand header-brand"><span class="dot"></span>TarnwickHub.com</div>
  <nav class="abs nav">
    <a class="active">Home</a><a>About us</a><a>Our Services</a><a>Latest News</a><a>Contact</a>
    <span class="search">Search</span><span class="search-btn"></span>
  </nav>

  <div class="abs hero-band"></div>
  <h1 class="abs hero-title">Welcome to TarnwickHub.com</h1>
  <div class="abs slide" role="img" aria-label="Photo of a hand sketching an idea, plan and action cycle on glass, a woman watching in soft focus"></div>
  <div class="abs arrow prev"><svg width="12" height="16" viewBox="0 0 12 16"><path d="M9 2 3 8l6 6" fill="none" stroke="#fff" stroke-width="3"/></svg></div>
  <div class="abs arrow next"><svg width="12" height="16" viewBox="0 0 12 16"><path d="M3 2l6 6-6 6" fill="none" stroke="#fff" stroke-width="3"/></svg></div>
  <div class="abs dots"><span class="on"></span><span></span><span></span></div>

  <div class="abs services-tab">
    <svg width="8" height="12" viewBox="0 0 8 12"><path d="M6 1 2 6l4 5" fill="none" stroke="#fff" stroke-width="2"/></svg>
    Services
    <svg width="8" height="12" viewBox="0 0 8 12"><path d="M2 1l4 5-4 5" fill="none" stroke="#fff" stroke-width="2"/></svg>
  </div>

  <div class="abs service active" style="left:35px">
    <div class="icon"><svg width="46" height="40" viewBox="0 0 46 40" fill="#0a2473"><circle cx="9" cy="8" r="5"/><circle cx="23" cy="6" r="6"/><circle cx="37" cy="8" r="5"/><rect x="3" y="15" width="12" height="22" rx="3"/><rect x="16" y="14" width="14" height="26" rx="3"/><rect x="31" y="15" width="12" height="22" rx="3"/></svg></div>
    <h3>DEVELOPMENT</h3>
    <p>Tax guides and books for multinational corporate teams.</p>
    <span class="btn">More Info</span>
  </div>
  <div class="abs service" style="left:214px">
    <div class="icon"><svg width="46" height="40" viewBox="0 0 46 40" fill="none" stroke="#7a7a7a"><circle cx="28" cy="15" r="8" stroke-width="6" stroke-dasharray="3 2.5"/><circle cx="28" cy="15" r="3" stroke-width="2"/><circle cx="12" cy="29" r="6" stroke-width="5" stroke-dasharray="2.5 2"/><circle cx="12" cy="29" r="2" stroke-width="2"/></svg></div>
    <h3>NEW BUSINESS</h3>
    <p>Predicting business and law issues before you expand abroad.</p>
    <span class="btn">More Info</span>
  </div>
  <div class="abs service" style="left:394px">
    <div class="icon"><svg width="46" height="40" viewBox="0 0 46 40" fill="#7a7a7a"><circle cx="23" cy="14" r="7"/><rect x="22" y="3" width="2" height="5"/><path d="M6 25h34v4H10v3h30v4H6z"/></svg></div>
    <h3>OUR PEOPLE</h3>
    <p>Written by tax advisers with decades of cross-border work.</p>
    <span class="btn">More Info</span>
  </div>
  <div class="abs service" style="left:572px">
    <div class="icon"><svg width="46" height="40" viewBox="0 0 46 40" fill="#7a7a7a" stroke="#fff" stroke-width="1.5"><ellipse cx="30" cy="34" rx="10" ry="4"/><ellipse cx="30" cy="28" rx="10" ry="4"/><ellipse cx="30" cy="22" rx="10" ry="4"/><ellipse cx="30" cy="16" rx="10" ry="4"/><ellipse cx="30" cy="10" rx="10" ry="4"/><ellipse cx="14" cy="34" rx="10" ry="4"/><ellipse cx="14" cy="28" rx="10" ry="4"/><ellipse cx="14" cy="22" rx="10" ry="4"/></svg></div>
    <h3>INCOME</h3>
    <p>Solve international business tax questions with confidence.</p>
    <span class="btn">More Info</span>
  </div>

  <div class="abs pager"><i></i><span><b>1</b> / 2</span><i></i></div>
  <div class="abs divider"></div>

  <section class="abs welcome">
    <h2>Welcome To Our Site</h2>
    <h4>Predicting and Solving Business and Law Issues for the Multinational</h4>
    <p>TarnwickHub.com sells information products for international corporate users. Our lead title, Silent Rivers and Quiet Orchard Lanes, covers international business tax, alongside Copperfield Monthly Digest and other books for advisers who work across borders.</p>
    <span class="btn navy">More Info</span>
  </section>
  <div class="abs office" role="img" aria-label="Photo of a smiling businesswoman in an office with colleagues at computers behind her"></div>

  <div class="abs newsletter"><h3>News Letter</h3></div>
  <div class="abs field nl-name">Your Name</div>
  <div class="abs field nl-mail">Email Adderss</div>
  <div class="abs subscribe">Subscribe</div>

  <footer class="abs footer"></footer>
  <div class="abs brand footer-brand"><span class="dot"></span>TarnwickHub.com</div>
  <p class="abs footer-about">TarnwickHub.com sells books and information products on international business tax, including Silent Rivers and Quiet Orchard Lanes and Copperfield Monthly Digest...</p>
  <div class="abs quick">
    <h5 class="col-title">Quick Link</h5>
    <ul><li>Home</li><li>About us</li><li>Our Services</li><li>Latest News</li><li>Contact</li></ul>
  </div>
  <div class="abs twitter">
    <h5 class="col-title">Twiter</h5>
    <div class="tw-field">Your Name</div>
    <div class="tw-field">Email Address</div>
  </div>
  <div class="abs contact">
    <svg width="26" height="24" viewBox="0 0 26 24" fill="#7a7a7a"><path d="M2 6c0-3 5-4 11-4s11 1 11 4v3h-6V7c-2-.5-8-.5-10 0v2H2z"/><path d="M6 11h14l3 10H3z"/><circle cx="13" cy="16" r="3" fill="#f3f3f3"/></svg>
    <p>0800-55501234<br>www.TarnwickHub.com</p>
  </div>
  <div class="abs bottom-strip"></div>
</div>
</body>
</html>
```